larvosk.net

We are a IT Service for the valley. I want a clean website, with new Design, like animated pictures. We focus on IT. Give me your best design. What I'm looking for is eye catching. Works with Smart Phones, and iPad, Tab. Need a section for Submit a support tickets and Remote support. I'm looking for new ideals. I'm open mind, let me see what you guys can do.

Target Market(s)

My clients to see what service and products we have.

Industry/Entity Type

It Service

Requirements
Must have
• Able to submit a trouble tickets and works with Smart Phones, iPad, Tab.

```html
<!DOCTYPE html>
<html lang="en">
<head>
<meta charset="utf-8">
<title>Larvosk Technology</title>
<link rel="stylesheet" href="https://fonts.googleapis.com/css2?family=Roboto+Condensed:wght@300;400;700&family=Arimo:wght@400;700&display=swap">
<style>
:root{
  --navy:#3b3b82;
  --navy-dark:#2c2c6b;
  --ink:#2b2b2b;
  --text:#555;
  --muted:#999;
  --strip:#b9b9c7;
  --hero-a:#f1f1f2;
  --hero-b:#dcdcde;
  --panel:#ececec;
  --card-a:#ffffff;
  --card-b:#e9e9e9;
  --footer:#e6e6e6;
}
*{box-sizing:border-box;margin:0;padding:0}
html,body{width:1200px;height:1028px;overflow:hidden;background:#fff}
body{position:relative;font-family:"Arimo",Arial,sans-serif;color:var(--text)}
a{text-decoration:none}

.site-header{position:absolute;left:0;top:0;width:1200px;height:135px;background:#fff}
.brand{position:absolute;left:40px;top:44px;display:flex;align-items:center;gap:10px}
.brand-mark{width:30px;height:30px;background:var(--navy);border-radius:50%}
.brand-name{font-family:"Roboto Condensed",sans-serif;font-weight:700;font-size:24px;color:var(--ink);letter-spacing:.5px}
.support-links{position:absolute;left:660px;top:16px;display:flex;gap:18px;font-family:"Roboto Condensed",sans-serif;font-weight:700;font-size:14px}
.support-links a{color:var(--navy)}
.support-links .sep{color:#ccc}
.quote-btn{position:absolute;left:984px;top:0;width:156px;height:49px;background:var(--navy);border-radius:0 0 4px 4px;display:flex;align-items:center;justify-content:center;gap:10px;color:#fff;font-family:"Roboto Condensed",sans-serif;font-weight:700;font-size:21px}
.main-nav a{position:absolute;top:85px;height:50px;line-height:58px;font-family:"Roboto Condensed",sans-serif;font-weight:700;font-size:18px;color:#a7a7a7}
.main-nav .active{left:716px;width:74px;text-align:center;background:linear-gradient(#e4e4e4,#f4f4f4);border-radius:4px 4px 0 0;color:var(--navy)}

.hero{position:absolute;left:0;top:135px;width:1200px;height:395px;background:linear-gradient(90deg,var(--hero-a),var(--hero-b) 70%,#e8e8ea)}
.hero-devices{position:absolute;left:72px;top:31px;width:530px;height:336px;background:linear-gradient(160deg,#3a3d44,#1b1c20 60%,#5a5e66);border-radius:14px}
.hero-title{position:absolute;left:664px;top:108px;font-family:"Roboto Condensed",sans-serif;font-weight:700;font-size:60px;color:var(--navy);line-height:1;white-space:nowrap}
.hero-sub{position:absolute;left:664px;top:178px;font-family:"Roboto Condensed",sans-serif;font-weight:300;font-size:59px;color:var(--ink);line-height:1}
.read-more{position:absolute;left:668px;top:258px;width:116px;height:38px;background:#1e1e1e;border-radius:3px;color:#fff;font-family:"Roboto Condensed",sans-serif;font-size:16px;line-height:38px;padding-left:12px}
.read-more span{position:absolute;right:0;top:0;width:26px;height:38px;background:#2c2c2c;border-radius:0 3px 3px 0;display:flex;align-items:center;justify-content:center}

.platform-strip{position:absolute;left:0;top:530px;width:1200px;height:85px;background:var(--strip)}
.platform{position:absolute;top:0;height:85px;display:flex;align-items:center;justify-content:center;border-right:1px solid #a9a9b8}
.platform.active{background:var(--navy-dark);border-right:none}

.services{position:absolute;left:36px;top:637px;width:294px;height:193px;background:#fff;border:1px solid #e2e2e2;box-shadow:0 1px 3px rgba(0,0,0,.08)}
.services h2{height:54px;background:var(--panel);padding-left:18px;line-height:56px;font-family:"Roboto Condensed",sans-serif;font-weight:700;font-size:24px;color:var(--navy)}
.services ul{list-style:none;padding:6px 0 0 14px}
.services li{height:31px;line-height:31px;font-size:13.5px;font-weight:700;color:#333;display:flex;align-items:center;gap:8px}
.services li::before{content:"";width:5px;height:5px;border-right:1.5px solid #777;border-top:1.5px solid #777;transform:rotate(45deg)}

.support{position:absolute;left:36px;top:855px;width:294px;height:97px;background:linear-gradient(90deg,var(--navy) 0,var(--navy) 65%,var(--navy-dark) 65%);border-radius:2px;color:#fff;font-family:"Roboto Condensed",sans-serif;font-weight:700}
.support .label{position:absolute;left:17px;top:14px;font-size:22px}
.support .phone{position:absolute;left:17px;top:46px;font-size:31px}
.support svg{position:absolute;right:22px;top:26px}

.welcome{position:absolute;left:352px;top:640px;width:788px}
.welcome h1{font-family:"Roboto Condensed",sans-serif;font-weight:700;font-size:26px;color:var(--navy);padding-bottom:6px;border-bottom:1px dashed #bbb}
.welcome p{margin-top:12px;font-size:12.5px;line-height:17px;color:#666;letter-spacing:.55px}

.feature{position:absolute;width:252px;background:linear-gradient(90deg,var(--card-a),var(--card-b));border:1px solid #e0e0e0;box-shadow:0 1px 2px rgba(0,0,0,.08);overflow:hidden}
.feature .badge{position:absolute;left:-14px;top:-4px;width:74px;height:66px;border-radius:50%;background:#e4e4e4;display:flex;align-items:center;justify-content:center;padding-left:12px}
.feature p{position:absolute;left:74px;top:14px;right:14px;font-size:12px;line-height:15.5px;color:#555}
.feature b{color:#444}

.site-footer{position:absolute;left:0;top:975px;width:1200px;height:53px;background:var(--footer);text-align:center;line-height:53px;font-size:12px;color:#888}
</style>
</head>
<body>
<header class="site-header">
  <div class="brand"><span class="brand-mark"></span><span class="brand-name">LARVOSK TECHNOLOGY</span></div>
  <div class="support-links">
    <a href="#ticket">Submit a Ticket</a><span class="sep">|</span><a href="#remote">Remote Support</a>
  </div>
  <a class="quote-btn">
    <svg width="16" height="20" viewBox="0 0 16 20"><path d="M2 2l7 8-7 8" fill="none" stroke="#8a8ad0" stroke-width="4"/></svg>
    Get a Quote
  </a>
  <nav class="main-nav">
    <a class="active">Home</a>
    <a style="left:827px">Services</a>
    <a style="left:944px">Products</a>
    <a style="left:1064px">Contact</a>
  </nav>
</header>

<section class="hero">
  <div class="hero-devices" role="img" aria-label="Tablets and phones displaying a colourful home screen"></div>
  <div class="hero-title">Mobile Phone &amp; Tab</div>
  <div class="hero-sub">Development</div>
  <a class="read-more">Read more<span><svg width="10" height="18" viewBox="0 0 10 18"><path d="M2 2l6 7-6 7" fill="none" stroke="#fff" stroke-width="1.5"/></svg></span></a>
</section>

<nav class="platform-strip">
  <a class="platform active" style="left:401px;width:87px"><svg width="44" height="44" viewBox="0 0 44 44"><rect x="6" y="6" width="32" height="32" rx="6" fill="#fff"/></svg></a>
  <a class="platform" style="left:488px;width:86px"><svg width="44" height="44" viewBox="0 0 44 44"><circle cx="22" cy="22" r="18" fill="#111"/></svg></a>
  <a class="platform" style="left:574px;width:99px"><svg width="64" height="52" viewBox="0 0 64 52"><rect x="3" y="3" width="58" height="36" fill="none" stroke="#111" stroke-width="6"/><rect x="26" y="39" width="12" height="6" fill="#111"/><rect x="16" y="45" width="32" height="4" fill="#111"/></svg></a>
  <a class="platform" style="left:673px;width:89px;border-right:none"><svg width="44" height="44" viewBox="0 0 44 44"><rect x="6" y="6" width="32" height="32" fill="#111"/></svg></a>
</nav>

<aside class="services">
  <h2>SERVICE OFFERINGS</h2>
  <ul>
    <li>Corvane VOIP Phones</li>
    <li>Desk Server</li>
    <li>Desk Workstation</li>
    <li>Web Design</li>
  </ul>
</aside>

<aside class="support">
  <div class="label">TECHNICAL SUPPORT</div>
  <div class="phone">555-014-2368</div>
  <svg width="48" height="44" viewBox="0 0 48 44"><path d="M4 14c0-8 40-8 40 0v4h-10v-4H14v4H4z" fill="#4e4e9a"/><path d="M12 18h24l6 22H6z" fill="#4e4e9a"/><circle cx="24" cy="29" r="7" fill="var(--navy-dark)"/><circle cx="24" cy="29" r="3" fill="#4e4e9a"/></svg>
</aside>

<main class="welcome">
  <h1>WELCOME</h1>
  <p>Founded in 2004, Larvosk Technology focus on quality of their products, along with their customer service to ensure both lengthy uptimes while also minimizing downtime.</p>
</main>

<article class="feature" style="left:352px;top:745px;height:89px">
  <div class="badge"><svg width="34" height="22" viewBox="0 0 34 22"><path d="M2 10c6-6 12-8 18-4l10-2c2 0 2 3 0 3l-8 2c4 2 6 5 4 7-6 2-16 4-24-2z" fill="#555"/></svg></div>
  <p><b>Accessibility</b> - On-Call and ready to serve your needs. Service is only a phone call away.</p>
</article>
<article class="feature" style="left:620px;top:745px;height:89px">
  <div class="badge"><svg width="34" height="30" viewBox="0 0 34 30"><path d="M2 4h12l3 3h15v21H2z" fill="#555"/><circle cx="17" cy="17" r="7" fill="#e4e4e4"/><path d="M17 12v5h4" stroke="#555" stroke-width="2" fill="none"/></svg></div>
  <p><b>Turn Around Time</b> - &nbsp;We Fix your network problem in a timely manner.</p>
</article>
<article class="feature" style="left:889px;top:745px;height:89px">
  <div class="badge"><svg width="34" height="32" viewBox="0 0 34 32"><path d="M17 1l4.5 10.5L33 12l-8.7 7.5L27 31l-10-6-10 6 2.7-11.5L1 12l11.5-.5z" fill="#555"/></svg></div>
  <p><b>Quality Products</b> - Provide hardware or software that will suit your specific needs.</p>
</article>
<article class="feature" style="left:352px;top:850px;height:79px">
  <div class="badge"><svg width="34" height="30" viewBox="0 0 34 30"><path d="M17 29C4 20 1 14 1 9a8 8 0 0116-2 8 8 0 0116 2c0 5-3 11-16 20z" fill="#555"/></svg></div>
  <p><b>Longevity</b> - &nbsp;Building a<br>long-term, trusting, relationship is our goal.</p>
</article>
<article class="feature" style="left:620px;top:850px;height:79px">
  <div class="badge"><svg width="36" height="30" viewBox="0 0 36 30"><circle cx="12" cy="8" r="6" fill="#555"/><path d="M0 28c0-8 5-12 12-12s12 4 12 12z" fill="#555"/><circle cx="25" cy="10" r="5" fill="#777"/><path d="M20 28c1-6 3-10 7-10s8 3 9 10z" fill="#777"/></svg></div>
  <p><b>Consultation</b> - We consult<br>you on proper upgrades or purchases for your company.</p>
</article>
<article class="feature" style="left:889px;top:850px;height:79px">
  <div class="badge"><svg width="34" height="32" viewBox="0 0 34 32"><rect x="9" y="1" width="16" height="11" fill="#555"/><path d="M17 12v6M5 18h24M5 18v4M29 18v4" stroke="#555" stroke-width="2" fill="none"/><rect x="0" y="22" width="11" height="9" fill="#555"/><rect x="23" y="22" width="11" height="9" fill="#555"/></svg></div>
  <p><b>Troubleshooting</b> - We will solve your network problems with a friendly smile.</p>
</article>

<footer class="site-footer">Larvosk Technology © 2012</footer>
</body>
</html>
```